Professional business cards for our auto wholesale dealership.

Target Market(s)

New and used cars sales managers and middle class to higher end private party buyers.

Industry/Entity Type

Automotive

Contact Information for Business Card

Bayline Premier Motors
Daniel R Whitcombe
Owner
(555) 417-3860
baypremmotors@mailbox-example.net
Dealer Lic # 48261

Logo Text

Bayline Premier Motors, Bay Prem Motors, BPM, etc

Font styles to use
Serif
Sans Serif

Colors

Designer to choose colors to be used in the design.

Requirements
Must have
• A professional, but not pretentious, look
Nice to have
• It might be nice to see "BPM" in a shape form i.e. circle, triangle, etc in the corner or background somehwere
Should not have
• bright "girly" colors

```html
<!DOCTYPE html>
<html lang="en">
<head>
<meta charset="UTF-8">
<title>Bayline Premier Motors — Business Card</title>
<link href="https://fonts.googleapis.com/css2?family=Source+Sans+3:wght@400;600&display=swap" rel="stylesheet">
<style>
  :root {
    --teal: #02667a;
    --ink: #1c1c1c;
    --paper: #ffffff;
    --backdrop: #c3c3c3;
  }
  * { margin: 0; padding: 0; box-sizing: border-box; }
  html, body {
    width: 1200px;
    height: 1200px;
    overflow: hidden;
    background: var(--backdrop);
    font-family: "Source Sans 3", Arial, sans-serif;
  }
  .card {
    position: absolute;
    left: 350px;
    width: 538px;
    height: 308px;
    background: var(--paper);
    overflow: hidden;
  }
  .card--front { top: 226px; }
  .card--back { top: 638px; }

  .holder {
    position: absolute;
    left: 37px;
    top: 48px;
    display: flex;
    align-items: center;
    white-space: nowrap;
  }
  .holder__name {
    color: var(--teal);
    font-size: 21px;
    font-weight: 400;
  }
  .holder__divider {
    width: 1.5px;
    height: 20px;
    background: var(--teal);
    margin: 0 13px;
  }
  .holder__role {
    color: var(--ink);
    font-size: 15px;
  }

  .contact {
    position: absolute;
    left: 276px;
    top: 192px;
    color: var(--ink);
    font-size: 14px;
    line-height: 22px;
  }
  .contact__line {
    display: flex;
    align-items: center;
    gap: 6px;
    white-space: nowrap;
  }
  .contact__line svg { width: 15px; height: 15px; flex: none; }
  .contact__licence { margin-top: 17px; }

  .wordmark {
    display: flex;
    align-items: center;
    gap: 10px;
    color: var(--teal);
    font-weight: 600;
    white-space: nowrap;
  }
  .wordmark__dot {
    border-radius: 50%;
    background: var(--teal);
    flex: none;
  }
  .card--front .wordmark {
    position: absolute;
    left: 28px;
    bottom: 30px;
    font-size: 40px;
    letter-spacing: 2px;
  }
  .card--front .wordmark__dot { width: 26px; height: 26px; }

  .card--back .wordmark {
    position: absolute;
    left: 50%;
    top: 50%;
    transform: translate(-50%, -50%);
    font-size: 28px;
  }
  .card--back .wordmark__dot { width: 30px; height: 30px; }
</style>
</head>
<body>
  <section class="card card--front">
    <div class="holder">
      <span class="holder__name">Daniel R Whitcombe</span>
      <span class="holder__divider"></span>
      <span class="holder__role">Owner</span>
    </div>

    <div class="contact">
      <div class="contact__line">
        <svg viewBox="0 0 16 16" aria-hidden="true"><path fill="var(--teal)" d="M10.5 1.5 12.5 3.3 10.6 5.4 9.2 4.5C7.6 6.3 6.4 8.6 6 11.2l1.6.4-.6 2.7-2.5-.5C3.9 9.6 6.1 4.9 10.5 1.5Z"/></svg>
        <span>(555) 417-3860</span>
      </div>
      <div class="contact__line">
        <svg viewBox="0 0 16 16" aria-hidden="true"><rect x="1" y="6" width="14" height="9" fill="var(--teal)"/><path d="M1 6l7 5 7-5" fill="none" stroke="#fff" stroke-width="1.2"/><circle cx="9" cy="3.5" r="2.3" fill="none" stroke="var(--teal)" stroke-width="1.2"/></svg>
        <span>baypremmotors@mailbox-example.net</span>
      </div>
      <div class="contact__licence">Dealer Lic # 48261</div>
    </div>

    <div class="wordmark">
      <span class="wordmark__dot"></span>
      <span>BPM</span>
    </div>
  </section>

  <section class="card card--back">
    <div class="wordmark">
      <span class="wordmark__dot"></span>
      <span>Bayline Premier Motors</span>
    </div>
  </section>
</body>
</html>
```